Updated Business Card Re-design (Logo Provided)

I am needing to update our business cards for our practice, Bright Harbor Care. We are a personal injury and wellness practice. The final design should be elegant and classy, but a type of card people would want to keep. Any samples should only have Dr. Tarek Minouvel on the template.
Updates

Went on vacation/holiday

Need extra days to review

Target Market(s)

Personal Injury clients, wellness clients

Industry/Entity Type

Personal Injury, medical, wellness

Contact Information for Business Card

dr and practice name, offerings

Requirements
Must have
• Single sided, this will be printed on a transparent business card, no exceptions.

```html
<!DOCTYPE html>
<html lang="en">
<head>
<meta charset="utf-8">
<title>Bright Harbor Care – Business Card</title>
<link rel="stylesheet" href="https://fonts.googleapis.com/css2?family=Montserrat:wght@400;500;700&display=swap">
<style>
  :root {
    --backdrop: #c9c9c9;
    --card: #f9f9f9;
    --blue: #1070b8;
    --orange: #f39322;
    --green: #2e8b4e;
    --ink: #1b1b1b;
    --white: #ffffff;
  }
  * { margin: 0; padding: 0; box-sizing: border-box; }
  html, body { width: 825px; height: 1200px; overflow: hidden; }
  body {
    background: var(--backdrop);
    font-family: "Montserrat", Arial, sans-serif;
    position: relative;
  }
  .business-card {
    position: absolute;
    left: 80px; top: 402px;
    width: 665px; height: 396px;
    background: var(--card);
    overflow: hidden;
  }
  .brand-mark {
    position: absolute;
    left: 36px; top: 62px;
    display: flex; align-items: center; gap: 8px;
    font-weight: 700; font-size: 17px;
    color: var(--green);
  }
  .brand-mark__dot {
    width: 26px; height: 26px; border-radius: 50%;
    background: var(--orange);
  }
  .practice-name {
    position: absolute;
    left: 31px; top: 132px;
    font-weight: 700; font-size: 25px; line-height: 26px;
    color: var(--blue);
    text-transform: uppercase;
  }
  .practice-tagline {
    position: absolute;
    left: 31px; top: 185px;
    font-weight: 500; font-size: 21px;
    color: var(--orange);
  }
  .doctor {
    position: absolute;
    left: 376px; top: 42px;
    white-space: nowrap;
  }
  .doctor__name {
    font-weight: 700; font-size: 18.5px; line-height: 24px;
    color: var(--orange);
  }
  .doctor__associate {
    font-weight: 500; font-size: 12px; line-height: 16px;
    color: var(--ink);
  }
  .doctor__rule {
    width: 122px; height: 2px; margin-top: 6px;
    background: var(--orange);
  }
  .contact-list {
    position: absolute;
    left: 376px; top: 101px;
    list-style: none;
  }
  .contact-list li {
    display: flex; align-items: center;
    height: 23px; margin-bottom: 5.5px;
    font-size: 13.5px; font-weight: 500; color: var(--ink);
    white-space: nowrap;
  }
  .contact-icon {
    width: 23px; height: 23px;
    border: 1.5px solid var(--orange);
    display: flex; align-items: center; justify-content: center;
    margin-right: 15px;
  }
  .services {
    position: absolute;
    left: 0; top: 222px;
    width: 100%; height: 106px;
    background: var(--green);
  }
  .service {
    position: absolute;
    display: flex; align-items: center;
    font-size: 16.5px; font-weight: 500; color: var(--white);
    white-space: nowrap;
  }
  .service__plus {
    width: 19px; height: 19px; border-radius: 50%;
    margin-right: 15px;
    flex: none;
  }
  .address {
    position: absolute;
    left: 0; top: 344px; width: 100%;
    display: flex; justify-content: center; align-items: center; gap: 12px;
    font-size: 14px; font-weight: 500; color: var(--blue);
    white-space: nowrap;
  }
</style>
</head>
<body>
  <article class="business-card">
    <div class="brand-mark"><span class="brand-mark__dot"></span>Bright Harbor Care</div>

    <h1 class="practice-name">Bright Harbor<br>Care</h1>
    <p class="practice-tagline">Lakeside Spine and Disc</p>

    <div class="doctor">
      <p class="doctor__name">Dr. Tarek Minouvel, D.C.</p>
      <p class="doctor__associate">Warren J Pellmore, PT, ATC, MS</p>
      <div class="doctor__rule"></div>
    </div>

    <ul class="contact-list">
      <li><span class="contact-icon"><svg width="12" height="12" viewBox="0 0 24 24"><path fill="#f39322" d="M6.6 10.8a15 15 0 0 0 6.6 6.6l2.2-2.2c.3-.3.7-.4 1-.2 1.1.4 2.3.6 3.6.6.6 0 1 .4 1 1V20c0 .6-.4 1-1 1A17 17 0 0 1 3 4c0-.6.4-1 1-1h3.5c.6 0 1 .4 1 1 0 1.3.2 2.5.6 3.6.1.3 0 .7-.2 1z"/></svg></span>555.014.2210</li>
      <li><span class="contact-icon"><svg width="12" height="12" viewBox="0 0 24 24"><rect x="6" y="2" width="12" height="20" rx="2" fill="none" stroke="#f39322" stroke-width="2"/><circle cx="12" cy="18" r="1.2" fill="#f39322"/></svg></span>555.014.7784</li>
      <li><span class="contact-icon"><svg width="13" height="10" viewBox="0 0 24 18"><rect width="24" height="18" fill="#f39322"/><path d="M0 0l12 10L24 0" fill="none" stroke="#fff" stroke-width="2"/></svg></span>info@brightharborcare.com</li>
      <li><span class="contact-icon"><svg width="13" height="13" viewBox="0 0 24 24" fill="none" stroke="#f39322" stroke-width="1.6"><circle cx="12" cy="12" r="10"/><ellipse cx="12" cy="12" rx="4.5" ry="10"/><path d="M2 12h20M4 6.5h16M4 17.5h16"/></svg></span>www.brightharborcare.com</li>
    </ul>

    <section class="services">
      <div class="service" style="left:36px;top:23px"><svg class="service__plus" viewBox="0 0 20 20"><circle cx="10" cy="10" r="10" fill="#1070b8"/><path d="M10 5v10M5 10h10" stroke="#fff" stroke-width="2.4"/></svg>Auto Accident Care</div>
      <div class="service" style="left:255px;top:23px"><svg class="service__plus" viewBox="0 0 20 20"><circle cx="10" cy="10" r="10" fill="#1070b8"/><path d="M10 5v10M5 10h10" stroke="#fff" stroke-width="2.4"/></svg>Medical Weight loss</div>
      <div class="service" style="left:504px;top:23px"><svg class="service__plus" viewBox="0 0 20 20"><circle cx="10" cy="10" r="10" fill="#1070b8"/><path d="M10 5v10M5 10h10" stroke="#fff" stroke-width="2.4"/></svg>Chiropractic</div>
      <div class="service" style="left:36px;top:61px"><svg class="service__plus" viewBox="0 0 20 20"><circle cx="10" cy="10" r="10" fill="#1070b8"/><path d="M10 5v10M5 10h10" stroke="#fff" stroke-width="2.4"/></svg>Primary Care</div>
      <div class="service" style="left:255px;top:61px"><svg class="service__plus" viewBox="0 0 20 20"><circle cx="10" cy="10" r="10" fill="#1070b8"/><path d="M10 5v10M5 10h10" stroke="#fff" stroke-width="2.4"/></svg>Physical Therapy</div>
    </section>

    <p class="address"><svg width="16" height="22" viewBox="0 0 16 22"><path d="M8 0a8 8 0 0 0-8 8c0 6 8 14 8 14s8-8 8-14a8 8 0 0 0-8-8z" fill="#1070b8"/><circle cx="8" cy="8" r="3.2" fill="#f9f9f9"/></svg>4820 Cedar Ridge Road, Suite 12 | Millbrook,GA 30000</p>
  </article>
</body>
</html>
```